A3 Event Poster for School Fundraiser

We are looking for a bold, engaging, and professional A3 poster design to promote a special school fundraising event. A top athlete will be visiting a primary school to inspire children, encourage participation in sport, and help launch a fundraising initiative to raise money for new PE/sports equipment for the school.

The poster will be displayed prominently outside the school and shared with parents and families. Its purpose is to generate excitement, explain the event quickly, and encourage parents/families to sponsor and get involved.

We work with about 50 different athletes so will need the design to be easy to alter the picture of the athlete/name etc so it can be replicated across the different athletes.

Target Market(s)

Priamary School Parents/Communities

Industry/Entity Type

Education

Font styles to use
Other font styles liked:
• The logo font is Rajdhani. ‘Corvel’ is bold, ‘Pennix’ is semibold and the strapline is regular.

Requirements
Must have
• Space for the Event Date (that school can write in themselves), A picture of the visiting athlete and their bio (with ability to easily change)
Nice to have
• Bold, eye-catching

```html
<!DOCTYPE html>
<html lang="en">
<head>
<meta charset="utf-8">
<title>Inspirational Athlete Visiting Our School – Poster</title>
<link href="https://fonts.googleapis.com/css2?family=League+Gothic&family=Oswald:wght@600&family=Poppins:wght@400;600;700;800&family=Rajdhani:wght@400;600;700&family=Permanent+Marker&display=swap" rel="stylesheet">
<style>
  :root{
    --backdrop:#6f2b83;
    --paper:#f7f6f7;
    --purple:#4f1a7f;
    --purple-soft:#7b4ca6;
    --red:#e0132e;
    --line:#b7a3cc;
    --white:#ffffff;
  }
  *{box-sizing:border-box;margin:0;padding:0}
  html,body{width:1200px;height:1200px;overflow:hidden;background:var(--backdrop)}
  .poster{position:absolute;left:185px;top:26px;width:830px;height:1147px;background:var(--paper);overflow:hidden;color:var(--purple)}
  .decor-bands{position:absolute;inset:0}
  .abs{position:absolute}

  .brand{left:56px;top:28px;display:flex;align-items:center;gap:8px}
  .brand-dot{width:50px;height:50px;border-radius:50%;background:var(--purple)}
  .brand-name{font-family:"Rajdhani",sans-serif;font-weight:700;font-size:62px;line-height:1;color:var(--purple);letter-spacing:-0.5px}
  .brand-tagline{left:116px;top:86px;font-family:"Rajdhani",sans-serif;font-weight:600;font-size:19px;color:var(--red)}

  .headline{font-family:"League Gothic",sans-serif;line-height:.85;text-transform:uppercase;transform:rotate(-4deg);transform-origin:left bottom;white-space:nowrap}
  .headline--top{left:71px;top:176px;font-size:92px;color:var(--purple)}
  .headline--main{left:52px;top:262px;font-size:168px;color:var(--purple)}
  .headline--sub{left:58px;top:432px;font-size:72px;color:var(--red)}
  .headline-rule{left:57px;top:496px;width:392px;height:12px}
  .spark{left:30px;top:146px;width:70px;height:58px}

  .icon-badge{border-radius:50%;background:var(--purple);display:flex;align-items:center;justify-content:center}
  .athlete-sport{left:58px;top:534px;width:70px;height:70px}
  .athlete-name{left:139px;top:530px;font-family:"Poppins",sans-serif;font-weight:700;font-size:33px;line-height:1.1;letter-spacing:.3px}
  .athlete-role{left:140px;top:572px;font-family:"Oswald",sans-serif;font-weight:600;font-size:22px;line-height:1.1;transform:scaleY(1.1);transform-origin:left top}
  .divider{height:1px;background:var(--line)}
  .divider--one{left:58px;top:636px;width:345px}
  .divider--two{left:58px;top:816px;width:297px}
  .bio-icon{left:59px;top:653px;width:64px;height:64px}
  .athlete-bio{left:137px;top:655px;width:262px;font-family:"Poppins",sans-serif;font-size:15.5px;line-height:20.4px;color:var(--purple)}
  .athlete-bio strong{font-weight:700;font-size:17.5px}

  .athlete-photo{left:477px;top:79px;width:353px;height:756px;background:linear-gradient(180deg,#e7d9cf 0%,#7a4e3a 18%,#c9452f 34%,#3452a8 55%,#e9eef8 80%,rgba(247,246,247,0) 100%);-webkit-mask:linear-gradient(180deg,#000 85%,transparent);mask:linear-gradient(180deg,#000 85%,transparent)}

  .appeal{left:113px;top:839px;width:637px;height:98px;border:2px solid var(--purple);display:flex;flex-direction:column;align-items:center;justify-content:center;font-family:"Poppins",sans-serif;font-weight:700;font-size:33px;line-height:1.12;letter-spacing:1.5px;text-transform:uppercase}
  .appeal-accent{color:var(--red)}

  .pillar{display:flex;align-items:center;gap:12px;top:947px}
  .pillar-icon{width:58px;height:58px}
  .pillar-icon--red{background:var(--red)}
  .pillar-label{font-family:"Oswald",sans-serif;font-weight:600;font-size:20px;line-height:1.1;text-transform:uppercase;color:#3b2355;padding-bottom:4px;border-bottom:2px solid transparent}
  .pillar-label .accent{color:var(--red)}
  .pillar--inspired{left:127px}
  .pillar--difference{left:346px}
  .pillar--difference .pillar-label{border-bottom-color:var(--red)}
  .pillar--active{left:587px}
  .pillar--active .pillar-label{border-bottom-color:var(--purple)}
  .pillar-sep{top:957px;width:1px;height:48px;background:var(--line)}

  .event-date{left:60px;top:1024px;width:725px;height:46px;border:1.5px solid var(--purple-soft);border-radius:6px}
  .event-date-label{left:84px;top:10px;font-family:"Poppins",sans-serif;font-weight:700;font-size:22px;line-height:1.1;letter-spacing:.3px}
  .event-date-line{left:259px;top:31px;width:445px;height:1px;background:var(--purple-soft)}
  .event-date-icon{left:32px;top:9px;width:28px;height:28px}

  .strap{left:36px;top:1087px;width:766px;height:42px}
  .strap-text{left:0;top:1097px;width:830px;text-align:center;font-family:"Permanent Marker",cursive;font-size:15.5px;color:var(--white);letter-spacing:.4px;text-transform:uppercase}
</style>
</head>
<body>
<main class="poster">
  <svg class="decor-bands" viewBox="0 0 830 1147" aria-hidden="true">
    <polygon points="395,716 830,233 830,262 415,716" fill="var(--red)"/>
    <polygon points="560,600 830,300 830,360 610,600" fill="var(--purple)"/>
    <polygon points="760,420 830,340 830,390 790,420" fill="var(--red)"/>
  </svg>

  <div class="athlete-photo abs" role="img" aria-label="Portrait photo of the visiting athlete in a red, white and blue national team tracksuit jacket"></div>

  <div class="brand abs"><span class="brand-dot"></span><span class="brand-name">CorvelPennix</span></div>
  <p class="brand-tagline abs">Inspiring every child</p>

  <svg class="spark abs" viewBox="0 0 70 58" aria-hidden="true">
    <g stroke="var(--red)" stroke-width="4" stroke-linecap="round">
      <line x1="6" y1="48" x2="22" y2="50"/>
      <line x1="4" y1="24" x2="26" y2="38"/>
      <line x1="26" y1="6" x2="40" y2="32"/>
      <line x1="56" y1="4" x2="54" y2="26"/>
    </g>
  </svg>

  <h1>
    <span class="headline headline--top abs">Inspirational</span>
    <span class="headline headline--main abs">Athlete</span>
    <span class="headline headline--sub abs">Visiting our school</span>
  </h1>
  <svg class="headline-rule abs" viewBox="0 0 392 12" aria-hidden="true">
    <path d="M2 11 C120 4 260 1 390 0 L390 4 C260 5 120 8 2 12 Z" fill="var(--purple)"/>
  </svg>

  <div class="athlete-sport icon-badge abs">
    <svg width="50" height="50" viewBox="0 0 50 50" fill="none" stroke="#fff" stroke-width="2.4">
      <circle cx="25" cy="25" r="21"/>
      <path d="M25 4 C19 16 20 26 26 33"/>
      <path d="M8 36 C18 30 30 30 43 35"/>
      <path d="M43 15 C32 17 26 24 26 33"/>
    </svg>
  </div>
  <h2 class="athlete-name abs">MARCUS ADEYEMI</h2>
  <p class="athlete-role abs">OLYMPIC VOLLEYBALL PLAYER</p>

  <div class="divider divider--one abs"></div>

  <div class="bio-icon icon-badge abs">
    <svg width="34" height="34" viewBox="0 0 34 34" fill="none" stroke="#fff" stroke-width="2">
      <circle cx="17" cy="11" r="7"/>
      <path d="M4 31 C4 23 10 20 17 20 C24 20 30 23 30 31 Z"/>
    </svg>
  </div>
  <p class="athlete-bio abs"><strong>Marcus</strong> is a dynamic English volleyball player and coach, known for his leadership on and off the court and his passion for inspiring the next generation through sport.</p>

  <div class="divider divider--two abs"></div>

  <div class="appeal abs">
    <span>Help us raise funds for</span>
    <span class="appeal-accent">New sports equipment</span>
  </div>

  <div class="pillar pillar--inspired abs">
    <div class="pillar-icon icon-badge">
      <svg width="34" height="34" viewBox="0 0 34 34" fill="none" stroke="#fff" stroke-width="2" stroke-linejoin="round"><path d="M17 3 L21 13 L31 13 L23 20 L26 30 L17 24 L8 30 L11 20 L3 13 L13 13 Z"/></svg>
    </div>
    <span class="pillar-label">Be<br>inspired</span>
  </div>
  <div class="pillar-sep abs" style="left:314px"></div>
  <div class="pillar pillar--difference abs">
    <div class="pillar-icon pillar-icon--red icon-badge">
      <svg width="34" height="34" viewBox="0 0 34 34" fill="none" stroke="#fff" stroke-width="2" stroke-linejoin="round"><path d="M17 20 C10 15 8 12 8 9.5 C8 7 10 5 12.5 5 C14.5 5 16 6.5 17 8 C18 6.5 19.5 5 21.5 5 C24 5 26 7 26 9.5 C26 12 24 15 17 20 Z"/><path d="M3 18 L10 26 L16 29 M31 18 L24 26 L18 29"/></svg>
    </div>
    <span class="pillar-label">Make a<br><span class="accent">difference</span></span>
  </div>
  <div class="pillar-sep abs" style="left:555px"></div>
  <div class="pillar pillar--active abs">
    <div class="pillar-icon icon-badge">
      <svg width="34" height="34" viewBox="0 0 34 34" fill="none" stroke="#fff" stroke-width="2.2" stroke-linecap="round" stroke-linejoin="round"><circle cx="22" cy="6" r="3"/><path d="M9 13 L15 10 L21 12 L18 20 L23 24 L21 31"/><path d="M21 12 L25 17 L30 16"/><path d="M18 20 L13 25 L6 25"/></svg>
    </div>
    <span class="pillar-label">Get<br>active</span>
  </div>

  <div class="event-date abs">
    <svg class="event-date-icon abs" viewBox="0 0 28 28" fill="none" stroke="var(--purple)" stroke-width="2"><rect x="3" y="5" width="22" height="20" rx="2"/><line x1="3" y1="11" x2="25" y2="11"/><line x1="9" y1="2" x2="9" y2="7"/><line x1="19" y1="2" x2="19" y2="7"/><g fill="var(--purple)" stroke="none"><rect x="7" y="14" width="3" height="3"/><rect x="12.5" y="14" width="3" height="3"/><rect x="18" y="14" width="3" height="3"/><rect x="7" y="19" width="3" height="3"/><rect x="12.5" y="19" width="3" height="3"/></g></svg>
    <span class="event-date-label abs">EVENT DATE:</span>
    <span class="event-date-line abs"></span>
  </div>

  <svg class="strap abs" viewBox="0 0 766 42" aria-hidden="true">
    <polygon points="0,8 60,4 766,6 726,20 766,36 60,42 30,30 50,22" fill="var(--purple)"/>
  </svg>
  <p class="strap-text abs">Inspiring every child to lead an active, resilient and healthy life</p>
</main>
</body>
</html>
```